Driving School
Brightlane Driving School
Project: Driving School
Driving School - Automotive
Creative Brief
Professional
214-52 Hollister Avenue Jamaica NY 11432
brightlanedriving@mailnest.example
www.BrightlaneDriving.example
Car & CDL Training
Calendar Or Driving school Directional MAP

```html
<!DOCTYPE html>
<html lang="en">
<head>
<meta charset="utf-8">
<title>Brightlane Driving School — Business Card</title>
<link rel="stylesheet" href="https://fonts.googleapis.com/css2?family=Michroma&display=swap">
<style>
  :root {
    --backdrop: #e9e6e2;
    --card: #ffffff;
    --brand-blue: #1f5591;
    --text-grey: #3a3a3a;
    --icon-fill: #2f5f98;
  }
  * { margin: 0; padding: 0; box-sizing: border-box; }
  html, body {
    width: 1200px;
    height: 902px;
    overflow: hidden;
    background: var(--backdrop);
  }
  .canvas {
    width: 1200px;
    height: 902px;
    display: flex;
    align-items: center;
    justify-content: center;
  }
  .business-card {
    position: relative;
    width: 1000px;
    height: 572px;
    background: var(--card);
    box-shadow: 0 6px 24px rgba(0, 0, 0, 0.12);
    font-family: "Michroma", "Eurostile", sans-serif;
  }
  .brand {
    position: absolute;
    top: 78px;
    left: 0;
    right: 0;
    display: flex;
    align-items: center;
    justify-content: center;
    gap: 16px;
  }
  .brand-dot {
    width: 22px;
    height: 22px;
    border-radius: 50%;
    background: var(--brand-blue);
  }
  .brand-name {
    font-size: 30px;
    color: var(--brand-blue);
    letter-spacing: 1px;
  }
  .person-name {
    position: absolute;
    top: 292px;
    left: 0;
    right: 0;
    text-align: center;
    font-size: 28px;
    letter-spacing: 3px;
    color: var(--brand-blue);
    text-transform: uppercase;
  }
  .contact {
    position: absolute;
    left: 0;
    right: 0;
    bottom: 66px;
    display: flex;
    flex-direction: column;
    align-items: center;
    gap: 10px;
    font-size: 12.5px;
    color: var(--text-grey);
    letter-spacing: 0.6px;
  }
  .contact-line {
    display: flex;
    gap: 14px;
    align-items: center;
  }
  .contact-item {
    display: flex;
    align-items: center;
    gap: 5px;
    white-space: nowrap;
  }
  .contact-icon {
    width: 14px;
    height: 14px;
    flex: none;
  }
</style>
</head>
<body>
<main class="canvas">
  <section class="business-card">
    <div class="brand">
      <span class="brand-dot"></span>
      <span class="brand-name">Brightlane Driving School</span>
    </div>

    <p class="person-name">Daniel Reyes</p>

    <div class="contact">
      <div class="contact-line">
        <span class="contact-item">
          <svg class="contact-icon" viewBox="0 0 14 14" aria-hidden="true">
            <circle cx="7" cy="7" r="7" fill="var(--icon-fill)"/>
            <path d="M7 3.2a2.4 2.4 0 0 0-2.4 2.4C4.6 7.4 7 10.8 7 10.8s2.4-3.4 2.4-5.2A2.4 2.4 0 0 0 7 3.2z" fill="#fff"/>
            <circle cx="7" cy="5.6" r="0.9" fill="var(--icon-fill)"/>
          </svg>
          214-52 Hollister Avenue Jamaica NY 11432
        </span>
        <span class="contact-item">
          <svg class="contact-icon" viewBox="0 0 14 14" aria-hidden="true">
            <circle cx="7" cy="7" r="7" fill="var(--icon-fill)"/>
            <path d="M4.6 3.6l1.3-.2.8 1.9-.9.7c.4.9 1.2 1.7 2.1 2.1l.7-.9 1.9.8-.2 1.3c-.1.4-.5.7-.9.7C6.2 10 4 7.8 3.9 4.5c0-.4.3-.8.7-.9z" fill="#fff"/>
          </svg>
          718-555-0147
        </span>
        <span class="contact-item">
          <svg class="contact-icon" viewBox="0 0 14 14" aria-hidden="true">
            <circle cx="7" cy="7" r="7" fill="var(--icon-fill)"/>
            <path d="M4.6 3.6l1.3-.2.8 1.9-.9.7c.4.9 1.2 1.7 2.1 2.1l.7-.9 1.9.8-.2 1.3c-.1.4-.5.7-.9.7C6.2 10 4 7.8 3.9 4.5c0-.4.3-.8.7-.9z" fill="#fff"/>
          </svg>
          718-555-0192
        </span>
      </div>
      <div class="contact-line">
        <span class="contact-item">
          <svg class="contact-icon" viewBox="0 0 14 14" aria-hidden="true">
            <circle cx="7" cy="7" r="7" fill="var(--icon-fill)"/>
            <rect x="3.6" y="4.6" width="6.8" height="4.8" fill="#fff"/>
            <path d="M3.6 4.6L7 7.3l3.4-2.7" fill="none" stroke="var(--icon-fill)" stroke-width="0.8"/>
          </svg>
          brightlanedriving@mailnest.example
        </span>
        <span class="contact-item">
          <svg class="contact-icon" viewBox="0 0 14 14" aria-hidden="true">
            <circle cx="7" cy="7" r="7" fill="var(--icon-fill)"/>
            <circle cx="7" cy="7" r="3.6" fill="none" stroke="#fff" stroke-width="0.9"/>
            <ellipse cx="7" cy="7" rx="1.5" ry="3.6" fill="none" stroke="#fff" stroke-width="0.8"/>
            <line x1="3.4" y1="7" x2="10.6" y2="7" stroke="#fff" stroke-width="0.8"/>
          </svg>
          www.BrightlaneDriving.example
        </span>
      </div>
    </div>
  </section>
</main>
</body>
</html>
```